Records Management Company Revamp

We are looking to revamp our web presence, and need a catchy design that helps us to get noticed! We would like the website to be in wordpress. the main requirements are a home page, a landing page template for SEO / PPC, and then a few other pages that can be reused throughout the website.

We are happy to supply content / video etc.
Updates

Low designer entries

Have guaranteed payment and hoping to receive more designs

Number of Pages Required

3 page

Other font styles liked:
• Find fonts listed in attached branding document

Requirements
Must have
• Home page as well as sub pages according to their colours. Need to use colours and fonts set out in branding guide. Attached are examples of home page and sub pages.
Nice to have
• We have uploaded some very basic ideas we have of how we wish the website to look, but looking to have it more professional and fit together. Please see uploaded items.

```html
<!DOCTYPE html>
<html lang="en">
<head>
<meta charset="utf-8">
<title>Vaultline Archives – Archive Document Storage &amp; Records Management</title>
<link rel="stylesheet" href="https://fonts.googleapis.com/css2?family=Oswald:wght@400;500;600&family=Open+Sans:wght@400;600;700&display=swap">
<style>
:root{
  --blue:#1e93d6;
  --blue-dark:#1b6f9e;
  --btn-dark:#1f5b82;
  --ink:#222;
  --text:#555;
  --muted:#888;
  --line:#dcdcdc;
  --pale:#eaf3f9;
  --footer:#333;
  --footer-bottom:#242424;
  --accent:#e0892a;
  --white:#fff;
}
*{box-sizing:border-box;margin:0;padding:0}
html,body{width:1200px;height:4444px;overflow:hidden}
body{position:relative;background:var(--white);font-family:"Open Sans",Arial,sans-serif;color:var(--text)}
.block{position:absolute;left:0;width:1200px}
.heading{font-family:"Oswald",Arial,sans-serif;font-weight:500;text-transform:uppercase;color:var(--ink);letter-spacing:.5px}
.photo{display:block}
.btn{display:inline-block;font-family:"Open Sans",Arial,sans-serif;font-weight:700;text-transform:uppercase;color:var(--white);background:var(--btn-dark);font-size:14px;letter-spacing:.5px;padding:16px 26px}

/* nav */
.site-nav{top:0;height:113px;background:var(--white);box-shadow:0 2px 6px rgba(0,0,0,.12);z-index:5}
.brand{position:absolute;left:76px;top:26px;display:flex;align-items:center;gap:10px}
.brand-mark{width:38px;height:38px;background:var(--blue)}
.brand-name{font-family:"Oswald",Arial,sans-serif;font-weight:500;font-size:30px;color:var(--blue-dark);text-transform:uppercase;line-height:1}
.menu{position:absolute;left:318px;top:0;height:113px;display:flex;list-style:none}
.menu li{height:113px;display:flex;align-items:center;padding:0 14px;font-size:13px;text-transform:uppercase;color:#8a8a8a;letter-spacing:.3px;white-space:nowrap}
.menu li.active{background:var(--blue);color:var(--white);font-weight:700;padding:0 22px}
.search{position:absolute;left:1108px;top:42px}

/* hero */
.hero{top:113px;height:627px;background:linear-gradient(180deg,#4a5058 0%,#2d3339 55%,#3a4047 100%)}
.hero-title{position:absolute;left:80px;top:176px;font-family:"Oswald",Arial,sans-serif;font-weight:500;font-size:44px;line-height:64px;color:var(--white);text-transform:uppercase;letter-spacing:1px}
.hero-sub{position:absolute;left:80px;top:318px;width:580px;font-size:21px;line-height:32px;color:var(--white)}
.quote-form{position:absolute;left:732px;top:94px;width:326px;height:400px;background:var(--white);border:3px solid var(--blue);padding:28px 22px}
.quote-form h3{font-family:"Oswald",Arial,sans-serif;font-weight:500;font-size:16px;line-height:24px;text-align:center;color:var(--ink);text-transform:uppercase;margin-bottom:20px}
.field-row{display:flex;gap:12px;margin-bottom:14px}
.field{flex:1;height:42px;border:1px solid var(--line);font-size:13px;color:#444;padding:12px 10px}
.field.tall{height:92px}
.quote-form .btn{display:block;width:148px;margin:8px auto 0;background:var(--btn-dark);font-size:14px;padding:13px 0;text-align:center;border:2px solid var(--blue)}

/* services */
.service-band{top:740px;height:282px;background:var(--pale)}
.services{top:676px;height:346px}
.service-card{position:absolute;top:0;width:252px;height:346px;background:var(--white);box-shadow:0 1px 5px rgba(0,0,0,.18);padding:8px}
.service-card .photo{height:207px}
.service-card h4{font-size:20px;font-weight:600;color:var(--blue);margin:16px 4px 8px}
.service-card p{font-size:13px;line-height:19px;color:var(--muted);margin:0 4px}

/* about */
.about{top:1081px;height:300px}
.about h2{position:absolute;left:80px;top:0;font-size:32px}
.about p{position:absolute;left:80px;top:62px;width:560px;font-size:14px;line-height:22px}
.about .btn{position:absolute;left:78px;top:248px}
.about .video{position:absolute;left:684px;top:0;width:436px;height:297px;background:linear-gradient(135deg,#5a6470,#2f353c)}
.play{position:absolute;left:684px;top:0;width:436px;height:297px;display:flex;align-items:center;justify-content:center}

/* how it works */
.how{top:1452px;height:696px;background:var(--white);border-top:1px solid #eee}
.how .person{position:absolute;left:133px;top:45px;width:385px;height:651px;background:linear-gradient(180deg,#cfc4b6,#9a7c5a 60%,#5a4636)}
.how h2{position:absolute;left:585px;top:60px;font-size:32px}
.step{position:absolute;left:585px;width:540px;display:flex;gap:22px}
.step-icon{width:64px;height:64px;background:var(--blue);flex:none;display:flex;align-items:center;justify-content:center}
.step h4{font-size:17px;font-weight:700;color:var(--blue-dark);margin:2px 0 6px}
.step p{font-size:13px;line-height:19px;color:var(--muted)}

/* team */
.team-band{top:2148px;height:415px;background:linear-gradient(135deg,#2a7fb6,#4aa1d4 50%,#2a78ad)}
.team-band h2{position:absolute;left:0;width:1200px;top:56px;text-align:center;color:var(--white);font-size:34px}
.team{top:2281px;height:347px}
.member{position:absolute;top:0;width:244px;height:347px;background:var(--white);box-shadow:0 1px 6px rgba(0,0,0,.2);padding:9px;text-align:center}
.member .photo{height:214px}
.member h4{font-size:20px;font-weight:700;color:var(--ink);margin:22px 0 16px;text-transform:uppercase}
.socials{display:flex;justify-content:center;gap:8px}
.socials span{width:28px;height:28px;border-radius:50%;border:1px solid #bbb}
.socials span:first-child{background:var(--blue);border-color:var(--blue)}

/* benefits */
.benefits{top:2696px;height:300px;text-align:center}
.benefits h2{font-size:34px;margin-top:10px}
.benefits .lead{width:720px;margin:24px auto 0;font-size:14px;line-height:24px}
.benefit-row{position:absolute;left:92px;top:164px;width:1016px;display:flex;justify-content:space-between}
.benefit{width:132px;height:148px;padding-top:24px;display:flex;flex-direction:column;align-items:center;gap:14px;font-size:15px;font-weight:700;color:var(--blue-dark);line-height:19px}
.benefit.featured{background:var(--blue);color:var(--white);border-radius:6px;border:3px solid #7cc3ea}

/* area of service */
.area{top:3081px;height:371px;background:var(--pale);text-align:center}
.area .map{position:absolute;left:260px;top:20px;width:680px;height:330px;background:radial-gradient(ellipse at center,rgba(160,196,222,.45),rgba(234,243,249,0) 70%)}
.area h2{position:relative;color:var(--blue);font-size:36px;padding-top:66px}
.area p{position:relative;width:700px;margin:30px auto 0;font-size:14px;line-height:23px}
.area .btn{position:absolute;left:517px;top:288px;padding:16px 26px;background:var(--btn-dark)}

/* testimonial */
.testimonial{top:3516px;height:470px;text-align:center}
.testimonial h2{font-size:34px;margin-top:22px}
.testimonial .mark{font-family:Georgia,serif;font-size:96px;line-height:70px;color:var(--blue);margin-top:28px;height:70px}
.testimonial blockquote{width:690px;margin:16px auto 0;font-size:15px;line-height:25px;color:var(--text)}
.testimonial cite{display:block;font-style:normal;font-weight:700;color:var(--accent);font-size:17px;margin-top:14px}
.arrow{position:absolute;top:190px}
.avatars{position:absolute;left:0;width:1200px;top:346px;height:110px;display:flex;justify-content:center;align-items:center;gap:32px}
.avatar{width:86px;height:86px;border-radius:50%;background:linear-gradient(135deg,#d8dde2,#a9b4be)}
.avatar.current{width:100px;height:100px;box-shadow:0 0 0 5px var(--white),0 0 0 8px var(--blue)}

/* footer */
.site-footer{top:4000px;height:380px;background:var(--footer);color:#ddd}
.footer-col{position:absolute;top:54px}
.footer-col h5{font-family:"Oswald",Arial,sans-serif;font-weight:500;font-size:17px;color:var(--blue);text-transform:uppercase;margin-bottom:22px;letter-spacing:.5px}
.site-footer .brand{position:static;margin-bottom:20px}
.site-footer .brand-name{color:var(--white)}
.footer-about p{font-size:13px;line-height:21px;width:230px}
.footer-socials{display:flex;gap:8px;margin-top:20px}
.footer-socials span{width:32px;height:32px;border-radius:50%;border:1px solid #888}
.footer-socials span:first-child{background:var(--blue);border-color:var(--blue)}
.footer-links{list-style:none;font-size:14px;line-height:28px}
.footer-links li::before{content:"• ";color:var(--white)}
.footer-links li.current{font-weight:700;color:var(--white)}
.contact-line{display:flex;gap:14px;font-size:14px;line-height:21px;margin-bottom:22px}
.contact-line strong{color:var(--blue);font-weight:600}
.footer-sub p{font-size:13px;line-height:21px;width:240px}
.email-box{width:240px;height:48px;background:var(--white);margin-top:16px;display:flex;align-items:center;gap:8px;padding:0 12px;font-size:13px;color:#777}
.footer-sub .btn{margin-top:16px;background:var(--blue);padding:14px 24px}
.copyright{top:4380px;height:64px;background:var(--footer-bottom);color:#ccc;font-size:13px;display:flex;align-items:center;justify-content:center}
.copyright b{color:var(--blue);font-weight:600;margin:0 4px}
</style>
</head>
<body>

<header class="block site-nav">
  <div class="brand"><span class="brand-mark"></span><span class="brand-name">Vaultline</span></div>
  <ul class="menu">
    <li class="active">Home</li><li>What we offer</li><li>How it works</li><li>Services</li><li>Team</li><li>Testimonial</li><li>Contact</li>
  </ul>
  <svg class="search" width="28" height="28" viewBox="0 0 28 28" aria-label="Search"><circle cx="11" cy="11" r="8" fill="none" stroke="#1e93d6" stroke-width="3"/><line x1="17" y1="17" x2="25" y2="25" stroke="#1e93d6" stroke-width="3" stroke-linecap="round"/></svg>
</header>

<section class="block hero" role="img" aria-label="Warehouse aisles stacked with archive boxes">
  <h1 class="hero-title">Archive Document Storage &amp;<br>Records Management</h1>
  <p class="hero-sub">Professional, secure and reliable, Vaultline Archives is your new home for all your archiving needs.</p>
  <form class="quote-form">
    <h3>Find out how cost effective we are in storing your archive boxes.</h3>
    <div class="field-row"><div class="field">Name :</div><div class="field">Phone :</div></div>
    <div class="field-row"><div class="field">Email :</div><div class="field">Number of Box :</div></div>
    <div class="field-row"><div class="field tall">Message / Comments :</div></div>
    <div class="btn">Submit Now</div>
  </form>
</section>

<div class="block service-band"></div>
<section class="block services">
  <article class="service-card" style="left:74px"><div class="photo" role="img" aria-label="Worker carrying archive box" style="background:linear-gradient(135deg,#d9c9b2,#a88a66)"></div><h4>Offsite Storage</h4><p>Store all your archives in our secure offsite warehouse</p></article>
  <article class="service-card" style="left:344px"><div class="photo" role="img" aria-label="Pile of shredded paper" style="background:linear-gradient(135deg,#e4e0da,#b9b1a5)"></div><h4>Document Shredding</h4><p>Lorem ipsum dolor sit amet, consectetur adipiscing elit.</p></article>
  <article class="service-card" style="left:608px"><div class="photo" role="img" aria-label="Business person with digital documents" style="background:linear-gradient(135deg,#c8d4de,#7f95a8)"></div><h4>Digitisation</h4><p>Lorem ipsum dolor sit amet, consectetur adipiscing elit.</p></article>
  <article class="service-card" style="left:872px"><div class="photo" role="img" aria-label="Stacked cardboard archive boxes" style="background:linear-gradient(135deg,#d6b58a,#9c6f3d)"></div><h4>Archiving Supplies</h4><p>Your one-stop shop for all your archiving needs. Shop Now!</p></article>
</section>

<section class="block about">
  <h2 class="heading">About Vaultline Archives</h2>
  <p>Lorem ipsum dolor sit amet, consectetur adipiscing elit, sed do eiusmod tempor incididunt ut labore et dolore magna aliqua. Ut enim ad minim veniam, quis nostrud exercitation ullamco laboris nisi ut aliquip ex ea commodo consequat. Duis aute irure dolor in reprehenderit in voluptate velit esse cillum dolore eu fugiat nulla pariatur. Excepteur sint occaecat cupidatat non proident, sunt in culpa qui officia deserunt mollit anim id est laborum.</p>
  <span class="btn">Read More</span>
  <div class="video" role="img" aria-label="Video still of warehouse staff handling boxes"></div>
  <div class="play"><svg width="70" height="70" viewBox="0 0 70 70"><circle cx="35" cy="35" r="31" fill="rgba(0,0,0,.25)" stroke="#1e93d6" stroke-width="4"/><path d="M28 22 L50 35 L28 48 Z" fill="#1e93d6"/></svg></div>
</section>

<section class="block how">
  <div class="person" role="img" aria-label="Smiling man holding archive boxes giving a thumbs up"></div>
  <h2 class="heading">How Vaultline Works</h2>
  <div class="step" style="top:122px"><div class="step-icon"><svg width="36" height="36" viewBox="0 0 36 36" fill="none" stroke="#fff" stroke-width="2.5"><path d="M4 11 L18 4 L32 11 L32 26 L18 33 L4 26 Z M4 11 L18 18 L32 11 M18 18 V33"/></svg></div><div><h4>We deliver boxes and Barcodes</h4><p>If you need them, we get you started with all the essentials<br>to prepare your archives.</p></div></div>
  <div class="step" style="top:226px"><div class="step-icon"><svg width="36" height="36" viewBox="0 0 36 36" fill="none" stroke="#fff" stroke-width="2.5"><rect x="7" y="4" width="22" height="28"/><path d="M12 12 H24 M12 18 H24 M12 24 H20"/></svg></div><div><h4>We pick up your documents</h4><p>When your boxes are ready, let us know and we'll come<br>by and collect your documents.</p></div></div>
  <div class="step" style="top:330px"><div class="step-icon"><svg width="36" height="36" viewBox="0 0 36 36" fill="none" stroke="#fff" stroke-width="2.5"><path d="M9 4 H22 L28 10 V32 H9 Z M22 4 V10 H28"/></svg></div><div><h4>We Store Your Documents</h4><p>Your documents are stored in our secure purpose-built<br>facility in Eastfield/Northgate.</p></div></div>
  <div class="step" style="top:434px"><div class="step-icon"><svg width="36" height="36" viewBox="0 0 36 36" fill="none" stroke="#fff" stroke-width="2.5"><rect x="5" y="8" width="26" height="22"/><path d="M5 14 H31 M11 4 V10 M25 4 V10 M13 22 L17 26 L24 19"/></svg></div><div><h4>We Retrieve &amp; Deliver Your Documents</h4><p>When you need your documents, just call or email us and<br>we'll get them to you!</p></div></div>
  <div class="step" style="top:538px"><div class="step-icon"><svg width="36" height="36" viewBox="0 0 36 36" fill="none" stroke="#fff" stroke-width="2.5"><rect x="5" y="12" width="26" height="10"/><path d="M10 12 V4 H26 V12 M10 22 V32 M15 22 V32 M21 22 V32 M26 22 V32"/></svg></div><div><h4>We Can Securely Destroy</h4><p>We can work with you on determining which documents<br>can be securely destroyed and do this for you!</p></div></div>
</section>

<section class="block team-band" role="img" aria-label="Blue-tinted warehouse backdrop"><h2 class="heading" style="color:#fff">Vaultline Teams</h2></section>
<section class="block team">
  <article class="member" style="left:80px"><div class="photo" role="img" aria-label="Staff member on forklift" style="background:linear-gradient(135deg,#e6cf6a,#9a8a48)"></div><h4>Alex Marlow</h4><div class="socials"><span></span><span></span><span></span><span></span></div></article>
  <article class="member" style="left:346px"><div class="photo" role="img" aria-label="Staff member carrying boxes" style="background:linear-gradient(135deg,#d9b48c,#8c6a48)"></div><h4>Alex Marlow</h4><div class="socials"><span></span><span></span><span></span><span></span></div></article>
  <article class="member" style="left:610px"><div class="photo" role="img" aria-label="Staff member in blue uniform with box" style="background:linear-gradient(135deg,#cfe3f1,#7eaed0)"></div><h4>Alex Marlow</h4><div class="socials"><span></span><span></span><span></span><span></span></div></article>
  <article class="member" style="left:876px"><div class="photo" role="img" aria-label="Staff member in black cap" style="background:linear-gradient(135deg,#e4e4e4,#5a5a5a)"></div><h4>Alex Marlow</h4><div class="socials"><span></span><span></span><span></span><span></span></div></article>
</section>

<section class="block benefits">
  <h2 class="heading">Vaultline Benefits</h2>
  <p class="lead">Lorem ipsum dolor sit amet, consectetur adipiscing elit, sed do eiusmod tempor incididunt ut labore et dolore magna aliqua enim ad minim veniam, quis nostrud exercitation.</p>
  <div class="benefit-row">
    <div class="benefit"><svg width="52" height="44" viewBox="0 0 52 44" fill="none" stroke="#444" stroke-width="2.5"><path d="M6 14 L26 6 L46 14 V34 L26 42 L6 34 Z M6 14 L26 22 L46 14 M26 22 V42"/></svg>Heading</div>
    <div class="benefit"><svg width="52" height="44" viewBox="0 0 52 44" fill="none" stroke="#444" stroke-width="2.5"><rect x="14" y="3" width="24" height="38"/><path d="M19 12 H33 M19 19 H33 M19 26 H33 M19 33 H27"/></svg>No lock-in contracts</div>
    <div class="benefit"><svg width="52" height="44" viewBox="0 0 52 44" fill="#444"><circle cx="26" cy="12" r="7"/><circle cx="12" cy="16" r="5"/><circle cx="40" cy="16" r="5"/><path d="M14 42 C14 28 38 28 38 42 Z M2 40 C2 28 18 28 16 34 L14 40 Z M50 40 C50 28 34 28 36 34 L38 40 Z"/></svg>Expert Staff</div>
    <div class="benefit featured"><svg width="56" height="44" viewBox="0 0 56 44" fill="none" stroke="#fff" stroke-width="2.5"><path d="M18 10 H40 V32 H18 Z M40 18 H48 L54 26 V32 H40"/><circle cx="24" cy="35" r="5" fill="#1e93d6"/><circle cx="46" cy="35" r="5" fill="#1e93d6"/><path d="M2 16 H12 M5 22 H13 M2 28 H12"/></svg>Speedy Retrievals</div>
    <div class="benefit"><svg width="52" height="44" viewBox="0 0 52 44" fill="none" stroke="#444" stroke-width="2.5"><rect x="6" y="4" width="40" height="28" rx="2"/><path d="M20 42 H32 M26 32 V42"/><circle cx="26" cy="18" r="7"/></svg>Simple Online Software</div>
    <div class="benefit"><svg width="52" height="44" viewBox="0 0 52 44" fill="none" stroke="#444" stroke-width="2.5"><circle cx="26" cy="22" r="19"/><path d="M32 14 C28 10 20 11 20 17 C20 23 32 21 32 27 C32 33 23 34 19 30 M26 8 V36"/></svg>Competitive Pricing</div>
    <div class="benefit"><svg width="52" height="44" viewBox="0 0 52 44" fill="none" stroke="#444" stroke-width="2.5"><path d="M8 16 H44 V40 H8 Z M14 16 V8 H38 V16"/><circle cx="26" cy="28" r="6"/></svg>Money Back Guarantee</div>
  </div>
</section>

<section class="block area">
  <div class="map" role="img" aria-label="Faint dotted world map"></div>
  <h2 class="heading" style="color:var(--blue)">Area of Services</h2>
  <p>Lorem ipsum dolor sit amet, consectetur adipiscing elit, sed do eiusmod tempor incididunt ut labore et dolore magna aliqua. Ut enim ad minim veniam, quis nostrud exercitation ullamco laboris nisi ut aliquip ex ea commodo consequat. Duis aute irure dolor in reprehenderit in voluptate velit esse cillum dolore eu fugiat nulla pariatur. Excepteur sint occaecat cupidatat non proident, sunt in culpa qui officia deserunt mollit anim id est laborum.</p>
  <span class="btn">Special Offer</span>
</section>

<section class="block testimonial">
  <h2 class="heading">Clients Testimonial</h2>
  <div class="mark">&ldquo;</div>
  <blockquote>Lorem Ipsum is simply dummy text of the printing and typesetting industry. Lorem Ipsum has been the industry's standard dummy text ever since the 1500s, when an unknown printer took a galley of type and scrambled it to make a type specimen book.</blockquote>
  <cite>- Jamie Rowe</cite>
  <svg class="arrow" style="left:62px" width="22" height="48" viewBox="0 0 22 48"><path d="M18 4 L4 24 L18 44" fill="none" stroke="#999" stroke-width="2.5"/></svg>
  <svg class="arrow" style="left:1116px" width="22" height="48" viewBox="0 0 22 48"><path d="M4 4 L18 24 L4 44" fill="none" stroke="#999" stroke-width="2.5"/></svg>
  <div class="avatars">
    <div class="avatar" role="img" aria-label="Client portrait"></div>
    <div class="avatar current" role="img" aria-label="Client portrait"></div>
    <div class="avatar" role="img" aria-label="Client portrait"></div>
  </div>
</section>

<footer class="block site-footer">
  <div class="footer-col footer-about" style="left:80px">
    <div class="brand"><span class="brand-mark"></span><span class="brand-name">Vaultline</span></div>
    <p>Lorem ipsum dolor sit amet, consectetur adipiscing elit, sed do eiusmod tempor incididunt ut labore et dolore magna aliqua. Ut enim ad commodo consequat.</p>
    <div class="footer-socials"><span></span><span></span><span></span><span></span></div>
  </div>
  <div class="footer-col" style="left:348px">
    <h5>Clients Testimonial</h5>
    <ul class="footer-links"><li class="current">Home</li><li>What we offer</li><li>How it works</li><li>Services</li><li>Team</li><li>Testimonial</li><li>Contact</li></ul>
  </div>
  <div class="footer-col" style="left:615px">
    <h5>Get in Touch</h5>
    <div class="contact-line"><svg width="18" height="24" viewBox="0 0 18 24"><path d="M9 1 C4 1 1 5 1 9 C1 15 9 23 9 23 C9 23 17 15 17 9 C17 5 14 1 9 1 Z" fill="#1e93d6"/><circle cx="9" cy="9" r="3" fill="#333"/></svg><div><strong>Vaultline Archives</strong><br>123, Address, State Name<br>City, Street, Zipcode</div></div>
    <div class="contact-line"><svg width="18" height="20" viewBox="0 0 18 20"><path d="M4 1 L8 5 L6 8 C7 11 9 13 12 14 L15 12 L18 16 L15 19 C8 19 1 11 1 4 Z" fill="#1e93d6"/></svg><div>123-456-7890</div></div>
    <div class="contact-line"><svg width="20" height="16" viewBox="0 0 20 16"><rect x="1" y="1" width="18" height="14" fill="#1e93d6"/><path d="M1 1 L10 9 L19 1" fill="none" stroke="#333" stroke-width="1.5"/></svg><div>info@vaultline-archives.com</div></div>
  </div>
  <div class="footer-col footer-sub" style="left:880px">
    <h5>Subscribe Newsletter</h5>
    <p>Would you like to receive exclusive access to articles, white papers and our regular monthly newsletter?</p>
    <div class="email-box"><svg width="16" height="12" viewBox="0 0 16 12"><rect x="1" y="1" width="14" height="10" fill="none" stroke="#777"/><path d="M1 1 L8 7 L15 1" fill="none" stroke="#777"/></svg>Enter Email Id</div>
    <span class="btn">Subscribe</span>
  </div>
</footer>
<div class="block copyright">Copyright &copy;<b>Vaultline Archives</b>- 2019 . All Right Reserved</div>

</body>
</html>
```